Velquora Design
Would like the design to go over the page in a way that can type over it.
We are a personal training and small group studio
Want it to be professional and classy
Updates
Project Deadline Extended
Reason: Asked for some modifications on a few designs, want to give the designers time to do this
Target Market(s)
All age groups, sports professionals as well as business professionals, families
Industry/Entity Type
Training
Requirements
Must have
- Must have Velquora Studio
Mina Tellaver
214 Barnicot Lane
Wexcombe Vale
South Australia 5173
Phone: 0438917263
Nice to have
- Professional classy fonts
Colour
Should not have
- Clip art
Balloons

```html
<!DOCTYPE html>
<html lang="en">
<head>
<meta charset="utf-8">
<title>Velquora Studio Letterhead</title>
<link rel="stylesheet" href="https://fonts.googleapis.com/css2?family=Archivo+Black&display=swap">
<style>
  :root {
    --orange: #ff6a0e;
    --orange-deep: #f25f00;
    --blue-dark: #0863c9;
    --blue-mid: #1c8ee8;
    --blue-light: #3b9bff;
    --sky: #5ccaf5;
    --navy: #0c3ea8;
    --white: #ffffff;
    --paper: #ffffff;
  }
  * { margin: 0; padding: 0; box-sizing: border-box; }
  html, body { width: 900px; height: 1200px; overflow: hidden; background: var(--paper); }
  .letterhead {
    position: relative;
    width: 900px;
    height: 1200px;
    background: var(--paper);
    font-family: "Archivo Black", "Arial Black", sans-serif;
  }
  .header-orange {
    position: absolute;
    left: 0; top: 0;
    width: 545px; height: 250px;
    background: linear-gradient(to bottom, var(--orange) 0%, var(--orange-deep) 68%, rgba(255,106,14,0.55) 84%, rgba(255,255,255,0) 100%);
  }
  .header-blue {
    position: absolute;
    left: 538px; top: 0;
    width: 362px; height: 222px;
    background: linear-gradient(to bottom, var(--sky) 0%, var(--blue-mid) 45%, rgba(28,142,232,0.6) 80%, rgba(255,255,255,0) 100%);
  }
  .brand {
    position: absolute;
    left: 40px; top: 92px;
    display: flex;
    align-items: center;
    gap: 18px;
  }
  .brand-mark {
    width: 46px; height: 46px;
    border-radius: 50%;
    background: var(--navy);
    flex: none;
  }
  .brand-name {
    font-size: 46px;
    line-height: 1;
    color: var(--navy);
    letter-spacing: 0.5px;
    white-space: nowrap;
  }
  .contact {
    position: absolute;
    left: 541px; top: 22px;
    list-style: none;
    color: var(--white);
    font-size: 20.5px;
    line-height: 25px;
    letter-spacing: 0.6px;
    text-shadow: 1px 1px 2px rgba(0, 20, 60, 0.85);
    white-space: nowrap;
  }
  .footer-bands {
    position: absolute;
    left: 0; bottom: 0;
    width: 900px; height: 43px;
    display: flex;
  }
  .band { height: 100%; }
  .band-orange { width: 289px; background: var(--orange); }
  .band-blue-dark { width: 284px; background: var(--blue-dark); }
  .band-blue-light { flex: 1; background: var(--blue-light); }
</style>
</head>
<body>
  <div class="letterhead">
    <div class="header-orange" role="img" aria-label="Orange brushed paint texture fading down into the page"></div>
    <div class="header-blue" role="img" aria-label="Blue brushed paint texture fading down into the page"></div>

    <div class="brand">
      <span class="brand-mark"></span>
      <span class="brand-name">Velquora Studio</span>
    </div>

    <ul class="contact">
      <li>Mina Tellaver</li>
      <li>214 Barnicot Lane</li>
      <li>Wexcombe Vale</li>
      <li>South Australia 5173</li>
      <li>Phone 0438917263</li>
      <li>South Australia 5173</li>
    </ul>

    <div class="footer-bands">
      <div class="band band-orange"></div>
      <div class="band band-blue-dark"></div>
      <div class="band band-blue-light"></div>
    </div>
  </div>
</body>
</html>
```